Banner for Vet Hospital 5m x 1.2m - Heat Stroke

Meadowlark Pet Hospital needs a Heat Stroke Banner for Summer.
The banner will be 5000mm long and 1200mm tall.

Our region has been hot this year and this summer is going to be extremely hot.
I want to warn people about heat stroke.
I want you to create a heat stroke banner that conveys the symptoms of heat stroke.

Pictures are better than words.
There should be IMAGES and WORDS that can be seen from the road 30m away and maybe some smaller words for people to read as they walk past.

Here are some of the signs of Heat Stroke:
- Panting which increases as heatstroke progresses
- Drooling, salivating
- Agitation, restlessness
- Very red or pale gums
- Bright red tongue
- Increased heart rate
- Breathing distress
- Vomiting Diarrhea (possibly with blood)
- Signs of mental confusion, delirium
- Dizziness, staggering
- Lethargy, weakness
- Muscle tremors
- Seizures
- Collapsing and lying down
- Little to no urine production
- Coma

I have attached characters that we often use in our advertising. They are optional.
I have done a mock up of the design I imagine. You could refine this design or make your own....or both.

Target Market(s)

Women aged 20 to 50.

Industry/Entity Type

Veterinary

Font styles to use
Sans Serif

Colors
fbed22
f78f20
ec1f27
ffffff

Requirements
Must have
• Heat Stroke Symtpms.
• Heat Stroke Warning.
• Summer theme.
Nice to have
• Bright colours.

```html
<!DOCTYPE html>
<html lang="en">
<head>
<meta charset="utf-8">
<title>Heat Stroke – Meadowlark Pet Hospital</title>
<link href="https://fonts.googleapis.com/css2?family=Lilita+One&family=Montserrat:wght@400;700;800&display=swap" rel="stylesheet">
<style>
  :root {
    --sun-yellow: #fbed22;
    --heat-orange: #f78f20;
    --alert-red: #ec1f27;
    --band-red: #de3a12;
    --white: #ffffff;
    --earth-brown: #6e4a30;
    --dog-brown: #8a6a55;
    --bubble: #ef915c;
    --ink: #2a1d14;
    --grass: #cfe7b8;
    --grass-deep: #b9dc9c;
  }
  * { margin: 0; padding: 0; box-sizing: border-box; }
  html, body { width: 1200px; height: 392px; overflow: hidden; background: var(--white); }
  .banner {
    position: relative; width: 1200px; height: 392px; overflow: hidden;
    background: linear-gradient(180deg, var(--white) 55%, #ededed 100%);
    font-family: "Montserrat", Arial, sans-serif;
  }
  .ground { position: absolute; left: 0; top: 0; }
  .headline {
    position: absolute; left: 30px; top: 92px;
    font-family: "Lilita One", "Arial Black", sans-serif;
    font-size: 74px; line-height: 0.98; color: var(--sun-yellow);
    -webkit-text-stroke: 7px var(--alert-red); paint-order: stroke fill;
    text-shadow: 4px 4px 0 #8c2a12;
    transform: skewX(-9deg);
  }
  .headline span { display: block; }
  .headline .line-two { margin-left: 42px; }
  .sun { position: absolute; left: 218px; top: 48px; }
  .contact-band {
    position: absolute; left: 0; top: 298px; width: 522px; height: 94px;
    background: var(--earth-brown);
    clip-path: polygon(0 0, 489px 0, 522px 100%, 0 100%);
    color: var(--white); font-size: 50px; padding: 16px 0 0 30px; letter-spacing: 0.5px;
  }
  .contact-band .label { font-weight: 400; }
  .contact-band .number { font-weight: 700; }
  .alert-strip { position: absolute; left: 510px; right: 0; top: 366px; height: 26px; background: var(--band-red); }
  .dog {
    position: absolute; border-radius: 46% 46% 30% 30%;
    background: radial-gradient(ellipse at 50% 40%, #a4877a, var(--dog-brown) 70%);
    opacity: 0.85;
  }
  .dog-panting { left: 436px; top: 80px; width: 106px; height: 208px; }
  .dog-vomiting { left: 668px; top: 80px; width: 170px; height: 214px; }
  .dog-collapsed { left: 958px; top: 168px; width: 162px; height: 106px; border-radius: 40% 50% 30% 30%; }
  .symptom {
    position: absolute; transform: translate(-50%, -50%);
    background: var(--bubble); border-radius: 50%;
    display: flex; align-items: center; justify-content: center; text-align: center;
    font-weight: 800; font-size: 10px; line-height: 1.15; color: var(--ink); text-transform: uppercase;
    box-shadow: 6px -4px 0 -2px var(--bubble), -6px 4px 0 -2px var(--bubble);
  }
  .arrow { position: absolute; }
  .thought-dot { position: absolute; background: var(--bubble); border-radius: 50%; }
</style>
</head>
<body>
<main class="banner">
  <svg class="ground" width="1200" height="392" viewBox="0 0 1200 392" aria-hidden="true">
    <path d="M390 300 C620 262 900 260 1200 270 L1200 366 L530 366 Z" fill="var(--grass)"/>
    <path d="M620 366 C800 318 1000 300 1200 300 L1200 366 Z" fill="var(--grass-deep)" opacity="0.6"/>
  </svg>

  <svg class="sun" width="120" height="120" viewBox="0 0 120 120" aria-hidden="true">
    <defs>
      <radialGradient id="sunGlow">
        <stop offset="55%" stop-color="#fff27a" stop-opacity="0.9"/>
        <stop offset="100%" stop-color="#fff27a" stop-opacity="0"/>
      </radialGradient>
      <radialGradient id="sunCore" cx="45%" cy="40%">
        <stop offset="0%" stop-color="var(--sun-yellow)"/>
        <stop offset="100%" stop-color="#f6c20e"/>
      </radialGradient>
    </defs>
    <circle cx="60" cy="60" r="58" fill="url(#sunGlow)"/>
    <circle cx="60" cy="60" r="40" fill="url(#sunCore)"/>
  </svg>

  <h1 class="headline"><span>Heat</span><span class="line-two">Stroke</span></h1>

  <div class="dog dog-panting" role="img" aria-label="Illustration of a sitting dog panting with its tongue out"></div>
  <div class="dog dog-vomiting" role="img" aria-label="Illustration of a dog vomiting and unwell"></div>
  <div class="dog dog-collapsed" role="img" aria-label="Illustration of a dog collapsed on the ground"></div>

  <div class="symptom" style="left:418px;top:92px;width:86px;height:56px;">Excessive<br>Painting</div>
  <div class="symptom" style="left:418px;top:170px;width:80px;height:46px;">Agitation</div>
  <div class="symptom" style="left:588px;top:90px;width:86px;height:52px;">Drooling</div>
  <div class="symptom" style="left:678px;top:120px;width:58px;height:36px;font-size:9px;">Diarrhea</div>
  <div class="symptom" style="left:728px;top:64px;width:76px;height:46px;font-size:9px;">Breathing<br>Distress</div>
  <div class="symptom" style="left:840px;top:88px;width:72px;height:46px;">Confusion</div>
  <div class="symptom" style="left:852px;top:177px;width:72px;height:46px;">Vomating</div>
  <div class="symptom" style="left:972px;top:108px;width:68px;height:46px;font-size:9px;">Muscles<br>Tremors</div>
  <div class="symptom" style="left:1064px;top:73px;width:84px;height:52px;">Collapse</div>
  <div class="symptom" style="left:1124px;top:142px;width:70px;height:42px;">Coma</div>

  <span class="thought-dot" style="left:986px;top:142px;width:12px;height:10px;"></span>
  <span class="thought-dot" style="left:1000px;top:158px;width:7px;height:6px;"></span>
  <span class="thought-dot" style="left:1048px;top:112px;width:14px;height:11px;"></span>
  <span class="thought-dot" style="left:1046px;top:132px;width:8px;height:7px;"></span>
  <span class="thought-dot" style="left:1086px;top:164px;width:12px;height:9px;"></span>
  <span class="thought-dot" style="left:1078px;top:178px;width:7px;height:6px;"></span>

  <svg class="arrow" style="left:542px;top:186px;" width="44" height="28" viewBox="0 0 44 28" aria-hidden="true">
    <path d="M0 9 H26 V0 L44 14 L26 28 V19 H0 Z" fill="var(--earth-brown)"/>
  </svg>
  <svg class="arrow" style="left:902px;top:186px;" width="44" height="28" viewBox="0 0 44 28" aria-hidden="true">
    <path d="M0 9 H26 V0 L44 14 L26 28 V19 H0 Z" fill="var(--earth-brown)"/>
  </svg>

  <div class="contact-band"><span class="label">Call: </span><span class="number">6500 2917</span></div>
  <div class="alert-strip"></div>
</main>
</body>
</html>
```